Business Card Design Project

we need a business card design for our company: www.dravonix.ch
It's important to include our already existing logo (see website)

```html
<!DOCTYPE html>
<html lang="en">
<head>
<meta charset="utf-8">
<title>Dravonix Business Card</title>
<link href="https://fonts.googleapis.com/css2?family=Ubuntu:wght@400;500&family=PT+Sans:wght@400&display=swap" rel="stylesheet">
<style>
  :root {
    --page-bg: #e6e6e3;
    --card-white: #ffffff;
    --brand-blue: #2f63b8;
    --brand-navy: #1c3f86;
    --accent-blue: #1d55c4;
    --card-black: #161616;
    --text-dark: #222222;
    --link-blue: #2a67c9;
    --text-light: #ffffff;
    --shadow: rgba(0, 0, 0, 0.18);
  }
  * { box-sizing: border-box; margin: 0; padding: 0; }
  html, body {
    width: 1200px;
    height: 944px;
    overflow: hidden;
    background: var(--page-bg);
  }
  .canvas {
    position: relative;
    width: 1200px;
    height: 944px;
  }
  .card {
    position: absolute;
    width: 620px;
    height: 400px;
    border-radius: 22px;
    background: var(--card-white);
    box-shadow: 0 10px 28px var(--shadow);
    overflow: hidden;
  }
  .card-front { left: 80px; top: 56px; }
  .card-back { left: 500px; top: 488px; }

  .wordmark {
    position: absolute;
    display: flex;
    align-items: center;
    gap: 14px;
    font-family: "Ubuntu", sans-serif;
    font-weight: 500;
    color: var(--brand-blue);
    letter-spacing: -1px;
  }
  .wordmark-square {
    display: block;
    background: var(--brand-navy);
  }
  .card-front .wordmark { left: 52px; top: 120px; font-size: 96px; }
  .card-front .wordmark-square { width: 58px; height: 58px; }
  .card-back .wordmark { left: 34px; top: 28px; font-size: 58px; }
  .card-back .wordmark-square { width: 34px; height: 34px; }

  .card-back-swoosh {
    position: absolute;
    inset: 0;
    width: 620px;
    height: 400px;
  }
  .contact {
    position: absolute;
    left: 38px;
    top: 128px;
    font-family: "PT Sans", sans-serif;
    color: var(--text-dark);
    font-size: 19px;
    line-height: 22px;
  }
  .contact-address { margin-bottom: 14px; }
  .contact-list { list-style: none; }
  .contact-list li {
    display: flex;
    align-items: center;
    gap: 12px;
    height: 24px;
  }
  .contact-list svg { width: 16px; height: 16px; flex: none; }
  .contact-web { color: var(--link-blue); }

  .person {
    position: absolute;
    right: 34px;
    bottom: 40px;
    text-align: right;
    font-family: "PT Sans", sans-serif;
    color: var(--text-light);
  }
  .person-name { font-size: 25px; line-height: 30px; }
  .person-role { font-size: 18px; line-height: 22px; }
</style>
</head>
<body>
<main class="canvas">

  <section class="card card-front" aria-label="Business card front">
    <div class="wordmark"><span class="wordmark-square"></span>Dravonix</div>
  </section>

  <section class="card card-back" aria-label="Business card back">
    <svg class="card-back-swoosh" viewBox="0 0 620 400" aria-hidden="true">
      <path d="M430 0 C385 190 305 330 170 400 L620 400 L620 0 Z" fill="var(--accent-blue)"/>
      <path d="M458 0 C418 200 340 340 212 400 L620 400 L620 0 Z" fill="var(--card-black)"/>
    </svg>

    <div class="wordmark"><span class="wordmark-square"></span>Dravonix</div>

    <div class="contact">
      <p class="contact-address">Dravonix AG<br>Lindenweg 12<br>8005 Zürich</p>
      <ul class="contact-list">
        <li>
          <svg viewBox="0 0 16 16" aria-hidden="true"><path d="M4 1.5 L6.5 1.5 L7.3 5 L5.6 6.2 C6.4 8 8 9.6 9.8 10.4 L11 8.7 L14.5 9.5 L14.5 12 C14.5 13.4 13.4 14.5 12 14.5 C6.5 14.2 1.8 9.5 1.5 4 C1.5 2.6 2.6 1.5 4 1.5 Z" fill="none" stroke="#333" stroke-width="1.4"/></svg>
          <span>+41 44 312 70 45</span>
        </li>
        <li>
          <svg viewBox="0 0 16 16" aria-hidden="true"><rect x="1.5" y="3.5" width="13" height="9" rx="1" fill="none" stroke="#333" stroke-width="1.4"/><path d="M1.8 4 L8 9 L14.2 4" fill="none" stroke="#333" stroke-width="1.4"/></svg>
          <span>info@dravonix.ch</span>
        </li>
        <li>
          <svg viewBox="0 0 16 16" aria-hidden="true"><circle cx="8" cy="8" r="6.3" fill="none" stroke="#333" stroke-width="1.4"/></svg>
          <span>dravonix.ch</span>
        </li>
        <li>
          <svg viewBox="0 0 16 16" aria-hidden="true"><rect x="1.5" y="2" width="13" height="9" rx="1" fill="none" stroke="#333" stroke-width="1.4"/><path d="M5 14 L11 14 M8 11 L8 14" stroke="#333" stroke-width="1.4"/></svg>
          <span class="contact-web">www.dravonix.ch</span>
        </li>
      </ul>
    </div>

    <div class="person">
      <p class="person-name">Lukas Berner</p>
      <p class="person-role">Manager</p>
    </div>
  </section>

</main>
</body>
</html>
```